Trade show flier

Need a two sided flier for a trade show that will go with the trade show banner you are designing for us. We have included some information we would like to see o the flier. We do need to work on the content. If you can start a design, we can work on the content. This must be done by 3/12/2018

Manufacturing companies

Trade

```html
<!DOCTYPE html>
<html lang="en">
<head>
<meta charset="utf-8">
<title>Meshline Systems – Trade Show Flier</title>
<link rel="stylesheet" href="https://fonts.googleapis.com/css2?family=Open+Sans:wdth,wght@75..100,400..700&family=Oswald:wght@400;500;600&display=swap">
<style>
  :root {
    --blue: #1b75bc;
    --blue-light: #8fbbe3;
    --orange: #f7821b;
    --ink: #2b2b2b;
    --footer: #161616;
    --page: #e9e6e1;
    --white: #ffffff;
    --badge: #c9ced4;
  }
  * { box-sizing: border-box; margin: 0; padding: 0; }
  html, body { width: 1200px; height: 797px; overflow: hidden; background: var(--page); }
  body { position: relative; font-family: "Open Sans", Arial, sans-serif; color: var(--ink); }

  .flier { position: absolute; top: 68px; width: 510px; height: 660px; background: var(--white); overflow: hidden; box-shadow: 0 6px 18px rgba(0,0,0,.25); }
  .flier--front { left: 60px; }
  .flier--back { left: 630px; }

  .photo { position: absolute; left: 0; top: 0; width: 510px; }
  .flier--front .photo { height: 285px; background: radial-gradient(circle at 75% 35%, #9a7a58 0%, #5b4634 35%, #2a2320 70%, #1a1614 100%); }
  .flier--back .photo { height: 262px; background: linear-gradient(120deg, #2c5f93 0%, #4c86bf 40%, #8fb4d6 70%, #c8d8e6 100%); }

  .shapes { position: absolute; left: 0; top: 0; }

  .headline { position: absolute; left: 12px; top: 48px; font-family: "Oswald", "Arial Narrow", sans-serif; font-weight: 500; font-size: 31px; line-height: 42px; color: var(--white); letter-spacing: -0.4px; text-transform: uppercase; }
  .headline .accent { color: var(--orange); }

  .panel-block { position: absolute; left: 12px; width: 203px; }
  .tab { display: inline-block; background: var(--orange); color: var(--white); font-size: 12px; padding: 3px 10px 3px 13px; width: 163px; margin-left: -7px; border-radius: 0 6px 6px 0; }
  .panel-text { margin-top: 5px; padding: 0 6px 0 8px; color: var(--white); font-size: 8.6px; line-height: 11.7px; text-align: justify; }
  .profile { top: 300px; }
  .vision { top: 425px; }
  .mission { top: 506px; }

  .brand { position: absolute; display: flex; align-items: center; gap: 10px; white-space: nowrap; }
  .brand__mark { width: 50px; height: 50px; border-radius: 50%; background: var(--blue); flex: none; }
  .brand__name { font-family: "Open Sans", Arial, sans-serif; font-weight: 700; font-size: 21px; color: var(--blue); letter-spacing: .2px; }
  .flier--front .brand { left: 237px; top: 283px; }
  .flier--back .brand { left: 22px; top: 277px; }

  .services-title { position: absolute; left: 240px; top: 352px; font-family: "Oswald", sans-serif; font-weight: 500; font-size: 20px; line-height: 26px; color: var(--orange); letter-spacing: .3px; }
  .services-title::after { content: ""; display: block; width: 102px; height: 2px; background: var(--blue); margin-top: 4px; }
  .services { position: absolute; left: 240px; top: 396px; width: 262px; list-style: none; }
  .services li { position: relative; padding-left: 18px; height: 21.5px; font-size: 6.6px; line-height: 7.8px; color: var(--ink); }
  .services li::before { content: ""; position: absolute; left: 1px; top: 1px; width: 10px; height: 10px; border-radius: 50%; background: var(--orange); }
  .services b { font-family: "Oswald", sans-serif; font-weight: 500; font-size: 8.4px; color: var(--blue); text-transform: uppercase; }

  .footer { position: absolute; left: 0; bottom: 0; width: 510px; height: 43px; background: linear-gradient(#2a2a2a, var(--footer)); color: var(--white); font-size: 10.8px; white-space: nowrap; display: flex; align-items: center; justify-content: center; }

  .support-badge { position: absolute; left: 384px; top: 211px; width: 120px; text-align: center; color: var(--white); font-weight: 700; font-size: 26px; line-height: 36px; }

  .plan-box { position: absolute; left: 15px; top: 357px; width: 478px; height: 199px; border: 1.3px solid var(--blue-light); border-radius: 8px; }
  .plan-title { position: absolute; left: 83px; top: 345px; width: 344px; height: 26px; background: var(--orange); color: var(--white); border-radius: 13px; font-size: 12.5px; display: flex; align-items: center; justify-content: center; }
  .plan-list { position: absolute; top: 382px; list-style: none; font-size: 8.8px; font-stretch: 87.5%; letter-spacing: -0.15px; line-height: 15.8px; color: var(--ink); white-space: nowrap; }
  .plan-list li::before { content: "• "; color: var(--orange); }
  .plan-list--left { left: 25px; }
  .plan-list--right { left: 254px; }
  .plan-note { position: absolute; left: 25px; top: 522px; width: 458px; font-size: 8.5px; line-height: 11.5px; text-align: justify; }

  .partners-title { position: absolute; left: 0; top: 566px; width: 510px; text-align: center; font-size: 8.5px; color: var(--ink); }
  .partners { position: absolute; left: 12px; top: 588px; width: 486px; display: flex; justify-content: space-between; align-items: center; }
  .partner { height: 16px; border-radius: 3px; background: var(--badge); }
</style>
</head>
<body>

<section class="flier flier--front">
  <div class="photo" role="img" aria-label="Factory worker in hard hat and safety vest taking notes on the production floor"></div>
  <svg class="shapes" width="510" height="660" aria-hidden="true">
    <rect x="0" y="230" width="12" height="430" fill="#ffffff"/>
    <path d="M12,262 Q110,244 215,235 L215,617 L12,617 Z" fill="var(--blue)"/>
    <path d="M215,251 Q360,232 510,272 L510,617 L215,617 Z" fill="var(--blue-light)"/>
    <path d="M215,257 Q360,238 510,278 L510,617 L215,617 Z" fill="#ffffff"/>
  </svg>

  <h1 class="headline">We <span class="accent">help</span> keep production<br>running by maximizing<br>network up-time</h1>

  <div class="panel-block profile">
    <div class="tab">COMPANY PROFILE</div>
    <p class="panel-text">Established in 2006, Meshline Systems is a Managed IT Service firm providing exceptional IT consultation and support for businesses in the California with 20 – 1000 employees. Our personable, reliable and professional team empowers our clients to make their IT infrastructure a strategic asset.</p>
  </div>
  <div class="panel-block vision">
    <div class="tab">OUR VISION</div>
    <p class="panel-text">To provide a customer experience that provides value and enables technology collaboration effortlessly.</p>
  </div>
  <div class="panel-block mission">
    <div class="tab">OUR MISSION</div>
    <p class="panel-text">Innovative collaboration to improve business process by leveraging technology that empowers organizations to implement a roadmap to success.</p>
  </div>

  <div class="brand">
    <span class="brand__mark"></span>
    <span class="brand__name">Meshline Systems</span>
  </div>

  <h2 class="services-title">OUR SERVICES</h2>
  <ul class="services">
    <li><b>Managed Services</b> - Proactive support, remediation and maintenance of your technology infrastructure, 24/7.</li>
    <li><b>Backup and Business Continuity</b> - Secure your data while minimizing downtime.</li>
    <li><b>Virtualization</b> - Increase IT flexibility and scalability while minimizing hardware resources.</li>
    <li><b>Voice Collaboration</b> - Voice-over-IP (VOIP) Design and Deployment.</li>
    <li><b>Cloud Services</b> - Leverage cloud support services for remote access and or business continuity.</li>
    <li><b>Security Services</b> - Multi-layered approach to addressing your network security.</li>
    <li><b>Wireless Services</b> - Secure connectivity and centralized management for wireless endpoint devices.</li>
    <li><b>Procurement Services</b> - Procurement of industry standard business class product.</li>
    <li><b>Project Collaboration</b> - Strategic technology roadmaps that address company business goals.</li>
    <li><b>Surveillance Services</b> - Intelligent network security video solutions.</li>
  </ul>

  <footer class="footer">For more information contact: sales@meshline-it.com&nbsp;|&nbsp;209-555-0142&nbsp;|&nbsp;www.meshline-it.com</footer>
</section>

<section class="flier flier--back">
  <div class="photo" role="img" aria-label="Engineer in hard hat working on a laptop beside an industrial control panel"></div>
  <svg class="shapes" width="510" height="660" aria-hidden="true">
    <path d="M0,240 Q250,262 510,246 L510,660 L0,660 Z" fill="var(--blue-light)"/>
    <path d="M0,247 Q250,270 510,254 L510,660 L0,660 Z" fill="#ffffff"/>
    <circle cx="366" cy="285" r="22" fill="var(--orange)"/>
    <circle cx="450" cy="248" r="82" fill="var(--orange)"/>
  </svg>

  <div class="support-badge">24x7<br>SUPPORT</div>

  <div class="brand">
    <span class="brand__mark"></span>
    <span class="brand__name">Meshline Systems</span>
  </div>

  <div class="plan-box"></div>
  <div class="plan-title">Our SteadyPath Managed Services Support include</div>
  <ul class="plan-list plan-list--left">
    <li>Team of industry certified Network Engineers</li>
    <li>Remote support (Weekdays 7am – 6pm)</li>
    <li>Onsite support (Weekdays 7am – 6pm)</li>
    <li>24x7 network monitoring and remediation.</li>
    <li>Daily proactive maintenance</li>
    <li>Managed antivirus software</li>
    <li>Managed ransomware protection</li>
    <li>Ticketing portal to track open tickets and resolutions</li>
  </ul>
  <ul class="plan-list plan-list--right">
    <li>Vendor management</li>
    <li>Network Documentation Management</li>
    <li>Software License Management</li>
    <li>Technology procurement</li>
    <li>Monitoring of existing backup systems and data recovery</li>
    <li>Business continuity planning</li>
    <li>Network and data security planning and testing</li>
    <li>Quarterly IT meetings</li>
  </ul>
  <p class="plan-note">We provide a great customer service experience with a simplified, cost-effective approach to IT that leverages certified technical professionals with industry standard skills and knowledge.</p>

  <p class="partners-title">OUR TECHNOLOGY PARTNERS</p>
  <div class="partners">
    <span class="partner" style="width:54px"></span>
    <span class="partner" style="width:38px"></span>
    <span class="partner" style="width:72px"></span>
    <span class="partner" style="width:56px"></span>
    <span class="partner" style="width:28px"></span>
    <span class="partner" style="width:74px"></span>
    <span class="partner" style="width:62px"></span>
    <span class="partner" style="width:58px"></span>
  </div>

  <footer class="footer">For more information contact: sales@meshline-it.com&nbsp;|&nbsp;209-555-0142&nbsp;|&nbsp;www.meshline-it.com</footer>
</section>

</body>
</html>
```